Business card for Bio pharmaceutical company

Hello,
We are a bio pharmaceutical contract manufacturing company in Brisbane, Australia. Can you please create a new business card design. Please go to our website for colours http://www.velocrine.com.au.
On the back can you include the cartoon mascot Tobin Wuzzle and the tagline
"A Global Biopharmaceutical Contract Development Manufacturing Company"
Target Market(s)
Biotechnology
Industry/Entity Type
Pharmaceutical
Contact Information for Business Card
Maria Hollingby
Business Development Manager
maria.hollingby@velocrine.com.au
1947 Kelmott Street Parvale Queesnland 4213 Australia
T: +61 7 3590 2481
M +61 427 516 093
F +61 7 3648 2057
www.velocrine.com.au
Look and feel

```html
<!DOCTYPE html>
<html lang="en">
<head>
<meta charset="utf-8">
<title>Velocrine Business Card</title>
<link rel="stylesheet" href="https://fonts.googleapis.com/css2?family=Exo+2:wght@400;500;600&display=swap">
<style>
  :root {
    --bg: #e6e7e9;
    --card-light: #ffffff;
    --card-shade: #e9eaec;
    --brand-blue: #0c5a7c;
    --brand-green: #b7cc3c;
    --ink: #2f3336;
    --ink-soft: #4a4e52;
  }
  html, body {
    margin: 0;
    width: 1200px;
    height: 900px;
    overflow: hidden;
    background: var(--bg);
    font-family: "Exo 2", "Segoe UI", sans-serif;
  }
  .card {
    position: absolute;
    left: 150px;
    top: 190px;
    width: 900px;
    height: 520px;
    border-radius: 46px;
    overflow: hidden;
    background: radial-gradient(ellipse at 45% 40%, var(--card-light) 0%, var(--card-light) 35%, var(--card-shade) 100%);
    box-shadow: 0 14px 40px rgba(0,0,0,0.18);
  }
  .card__waves {
    position: absolute;
    inset: 0;
  }
  .brand {
    position: absolute;
    left: 62px;
    top: 180px;
    display: flex;
    align-items: center;
    gap: 14px;
  }
  .brand__name {
    font-size: 76px;
    font-weight: 600;
    color: var(--brand-blue);
    letter-spacing: -1px;
    line-height: 1;
  }
  .brand__mark {
    width: 22px;
    height: 22px;
    background: var(--brand-green);
    margin-top: -46px;
  }
  .person {
    position: absolute;
    right: 62px;
    top: 40px;
    text-align: right;
    color: var(--ink);
  }
  .person__name {
    font-size: 22px;
    font-weight: 500;
    letter-spacing: 2px;
  }
  .person__title {
    font-size: 14px;
    font-weight: 500;
    letter-spacing: 2px;
    margin-top: 2px;
  }
  .contacts {
    position: absolute;
    right: 62px;
    top: 112px;
    list-style: none;
    margin: 0;
    padding: 0;
    color: var(--ink-soft);
    font-size: 15px;
    letter-spacing: 1px;
    text-align: right;
  }
  .contacts li {
    display: flex;
    justify-content: flex-end;
    align-items: center;
    gap: 8px;
    height: 25px;
  }
  .contacts svg {
    width: 16px;
    height: 16px;
    flex: none;
    fill: none;
    stroke: var(--ink);
    stroke-width: 1.8;
  }
  .contacts .contacts__web { padding-right: 14px; }
  .address {
    position: absolute;
    left: 62px;
    top: 320px;
    font-size: 19px;
    font-weight: 500;
    letter-spacing: 1.5px;
    color: var(--ink);
    line-height: 1.45;
  }
</style>
</head>
<body>
  <div class="card">
    <svg class="card__waves" viewBox="0 0 900 520" preserveAspectRatio="none" aria-hidden="true">
      <path d="M0,420 C300,445 700,400 900,300 L900,520 L0,520 Z" fill="var(--brand-blue)"/>
      <path d="M0,420 C300,445 700,400 900,300 L900,286 C700,388 300,432 0,408 Z" fill="#ffffff"/>
      <path d="M160,404 C470,404 720,360 900,262 L900,280 C720,376 470,416 160,404 Z" fill="var(--brand-green)"/>
    </svg>

    <div class="brand">
      <span class="brand__name">Velocrine</span>
      <span class="brand__mark"></span>
    </div>

    <div class="person">
      <div class="person__name">DORIAN FELIKS</div>
      <div class="person__title">PRESIDENT</div>
    </div>

    <ul class="contacts">
      <li>012 345 6789
        <svg viewBox="0 0 16 16"><path d="M3 2 L6 2 L7 5 L5 6.5 C6 9 7 10 9.5 11 L11 9 L14 10 L14 13 C8 14 2 8 3 2 Z"/></svg>
      </li>
      <li>012 345 6789
        <svg viewBox="0 0 16 16"><rect x="4" y="1.5" width="8" height="13" rx="1.5"/><line x1="7" y1="12" x2="9" y2="12"/></svg>
      </li>
      <li>012 345 6789
        <svg viewBox="0 0 16 16"><rect x="2" y="6" width="12" height="8" rx="1"/><rect x="5" y="2" width="6" height="4"/></svg>
      </li>
      <li>012 345 6789
        <svg viewBox="0 0 16 16"><rect x="1.5" y="3.5" width="13" height="9"/><polyline points="1.5,3.5 8,9 14.5,3.5"/></svg>
      </li>
      <li>urname@email.com
        <svg viewBox="0 0 16 16"><circle cx="8" cy="8" r="6.5"/><ellipse cx="8" cy="8" rx="3" ry="6.5"/><line x1="1.5" y1="8" x2="14.5" y2="8"/></svg>
      </li>
      <li class="contacts__web">www.urwebsitename.com</li>
    </ul>

    <div class="address">047.12th floor,Plaza<br>Harbour Road LKG</div>
  </div>
</body>
</html>
```